International Chino Pant Manufacturer

We need modern packaging design for men's chino. All kinds of packaging designs are welcome.

The pant is folded and packaged in a poly bag. We require a label design for the brand name Korvell. The main label will be attached by a string on the belt loop. the size of that label will 15cm in length and 5cm wide. This is the first label the customer see's when he picks up the garment. Therefore, we require an eye catching design for that. If required it could have certain information about the chino pant on the main label such as Comfort fit, Wrinkle-resistant, machine washable, luxury fabric. But, if you feel that adding the above information spoils the design of the label then it is not a must to include the above information. On the back of the label we like to include the information that this pant was manufactured in an Ecora Summit certified green plant and hence the damage to the environment because of the plant is nill.

The second label label is attached on to the waist band and the purpose of that label is to include the size of the pant such 32x32. The size of that label is 8cm in length and 4cm in width. There is no design on the back on this label it has to be blank.

Manufacturer

```html
<!DOCTYPE html>
<html lang="en">
<head>
<meta charset="utf-8">
<title>Korvell Chino – Hang Tag</title>
<link rel="stylesheet" href="https://fonts.googleapis.com/css2?family=Oswald:wght@600&display=swap">
<style>
  :root {
    --page: #ffffff;
    --tag-top: #e9bd92;
    --tag-mid: #d8947a;
    --tag-low: #c96e5c;
    --tag-base: #cf8473;
    --ink-brand: #6a2d1a;
    --ink-copy: #5a1d18;
    --figure: #5e2a17;
    --figure-soft: #7a3b24;
  }
  * { margin: 0; padding: 0; box-sizing: border-box; }
  html, body {
    width: 1200px;
    height: 1196px;
    overflow: hidden;
    background: var(--page);
  }
  .hang-tag {
    position: absolute;
    left: 415px;
    top: 42px;
    width: 368px;
    height: 1110px;
    overflow: hidden;
    background:
      radial-gradient(ellipse at 30% 12%, rgba(245, 210, 160, 0.8), transparent 55%),
      radial-gradient(ellipse at 75% 45%, rgba(200, 110, 90, 0.45), transparent 60%),
      linear-gradient(180deg, var(--tag-top) 0%, var(--tag-mid) 38%, var(--tag-low) 70%, var(--tag-base) 100%);
  }
  .brand-name {
    position: absolute;
    left: 212px;
    top: 14px;
    writing-mode: vertical-rl;
    font-family: "Oswald", sans-serif;
    font-weight: 600;
    font-size: 120px;
    line-height: 1;
    letter-spacing: 6px;
    text-transform: uppercase;
    color: var(--ink-brand);
  }
  .moose-figure {
    position: absolute;
    left: 35px;
    top: 592px;
    width: 300px;
    height: 300px;
  }
  .feature-list {
    position: absolute;
    left: 20px;
    top: 902px;
    list-style: none;
    font-family: "Oswald", sans-serif;
    font-weight: 600;
    font-size: 40px;
    line-height: 45px;
    letter-spacing: 0.4px;
    color: var(--ink-copy);
    text-transform: uppercase;
    white-space: nowrap;
  }
</style>
</head>
<body>
  <main class="hang-tag">
    <h1 class="brand-name">Korvell</h1>

    <svg class="moose-figure" viewBox="0 0 300 300" role="img" aria-label="Silhouette of a moose standing on a small hilltop">
      <defs>
        <radialGradient id="figureFill" cx="55%" cy="50%" r="65%">
          <stop offset="0%" stop-color="var(--figure)" stop-opacity="0.85"/>
          <stop offset="100%" stop-color="var(--figure-soft)" stop-opacity="0"/>
        </radialGradient>
      </defs>
      <rect x="0" y="0" width="300" height="300" rx="40" fill="url(#figureFill)"/>
    </svg>

    <ul class="feature-list">
      <li>Comfort Fit</li>
      <li>Wrinkle-Resistant</li>
      <li>Machine Washable</li>
      <li>Luxury Fabric</li>
    </ul>
  </main>
</body>
</html>
```